Real Estate Open House A Frame Sign

The sign is 22" wide and 28" tall. This sign is used to post around the neighbourhood to direct people to an open house (home that is for sale). It is also used for self-promotion.

Designwise
- I just want something with a modern look, simple and clean.
- I want my picture and business logo on the left side.
- On the right side, website (www.lumwick-realestate.com) and my phone (555-374-9126), then a blank space where I can write an address when I need to.

I'm not sure how I want the overall design look. I'm very open-minded and I'm depending on your creative mind to come up with something.

If you have any questions, please let me know.

```html
<!DOCTYPE html>
<html lang="en">
<head>
<meta charset="utf-8">
<title>Open House Sign – Lumwick Real Estate</title>
<link href="https://fonts.googleapis.com/css2?family=Lato:wght@300;400;700;900&display=swap" rel="stylesheet">
<style>
  :root {
    --backdrop: #eceef1;
    --grey-dark: #68686b;
    --grey-light: #9a9a9d;
    --navy: #1b3f7a;
    --navy-deep: #13295a;
    --white: #ffffff;
    --suit: #2c3038;
    --suit-light: #4a4f58;
  }
  * { margin: 0; padding: 0; box-sizing: border-box; }
  html, body {
    width: 1200px; height: 800px; overflow: hidden;
    background: var(--backdrop);
    font-family: "Lato", sans-serif;
  }
  .sign {
    position: absolute;
    left: 301px; top: 20px;
    width: 597px; height: 760px;
    overflow: hidden;
    box-shadow: 0 6px 20px rgba(0,0,0,0.18);
  }
  .sign-art { position: absolute; inset: 0; width: 100%; height: 100%; }
  .headline {
    position: absolute; right: 32px; top: 44px;
    color: var(--navy-deep);
    font-weight: 900; font-size: 71px; line-height: 0.92;
    text-align: right; letter-spacing: -1px;
  }
  .address {
    position: absolute; right: 30px; top: 212px;
    text-align: right; color: var(--white);
  }
  .address-label { font-weight: 700; font-size: 18px; line-height: 1.2; margin-bottom: 2px; }
  .address-lines { font-weight: 300; font-size: 15.5px; line-height: 19.5px; }
  .brand {
    position: absolute; right: 30px; top: 622px;
    text-align: right; color: var(--white);
  }
  .brand-name { font-weight: 300; font-size: 46px; line-height: 1; letter-spacing: 2px; }
  .brand-sub { font-weight: 400; font-size: 14px; letter-spacing: 0.5em; margin-top: 6px; margin-right: -0.5em; }
  .contact-web { font-weight: 700; font-size: 15px; margin-top: 12px; }
  .contact-phone {
    font-weight: 700; font-size: 19px; margin-top: 4px;
    display: flex; align-items: center; justify-content: flex-end; gap: 6px;
  }
  .contact-phone svg { width: 15px; height: 15px; }
</style>
</head>
<body>
  <div class="sign">
    <svg class="sign-art" viewBox="0 0 742 940" preserveAspectRatio="none" aria-hidden="false">
      <defs>
        <linearGradient id="bgGrad" x1="0" y1="0" x2="1" y2="1">
          <stop offset="0" stop-color="#5f5f62"/>
          <stop offset="0.6" stop-color="#8a8a8d"/>
          <stop offset="1" stop-color="#a3a3a6"/>
        </linearGradient>
        <linearGradient id="agentGrad" x1="0" y1="0" x2="0" y2="1">
          <stop offset="0" stop-color="#3a3d44"/>
          <stop offset="0.35" stop-color="var(--suit-light)"/>
          <stop offset="1" stop-color="var(--suit)"/>
        </linearGradient>
      </defs>
      <rect class="sign-bg" width="742" height="940" fill="url(#bgGrad)"/>
      <rect class="house-sketch" role="img" aria-label="Faint line sketch of a house behind the agent" x="0" y="20" width="470" height="520" fill="#ffffff" opacity="0.06"/>
      <path class="curve-white" d="M0,540 Q210,390 430,405 Q600,418 742,470 L742,940 L0,940 Z" fill="var(--white)"/>
      <path class="curve-line" d="M395,412 Q580,440 742,525" fill="none" stroke="var(--navy)" stroke-width="4"/>
      <path class="curve-navy" d="M0,580 Q230,470 430,485 Q610,505 742,640 L742,940 L0,940 Z" fill="var(--navy)"/>
      <path class="agent-photo" role="img" aria-label="Portrait photo of the agent in a dark suit and tie, arms crossed, smiling"
        d="M150,110 Q260,60 350,140 Q380,230 350,370 Q470,420 520,560 L500,940 L0,940 L0,640 Q60,470 200,440 Q150,340 150,110 Z"
        fill="url(#agentGrad)"/>
    </svg>

    <h1 class="headline">OPEN<br>HOUSE</h1>

    <div class="address">
      <div class="address-label">ADDRESS</div>
      <div class="address-lines">Lorem ipsum dolor sit amet,<br>consectetur adipiscing elit,<br>sed do eiusmod tempor</div>
    </div>

    <div class="brand">
      <div class="brand-name">LUMWICK</div>
      <div class="brand-sub">REAL ESTATE</div>
      <div class="contact-web">www.lumwick-realestate.com</div>
      <div class="contact-phone">
        <svg viewBox="0 0 16 16" aria-hidden="true">
          <circle cx="8" cy="8" r="8" fill="#ffffff"/>
          <path d="M5.2,3.8 L6.6,3.6 L7.3,5.8 L6.4,6.6 Q7.1,8.4 9.2,9.6 L10.1,8.7 L12.2,9.4 L12,10.9 Q11.6,12.2 10.2,12 Q5.2,11 4,5.6 Q3.9,4.2 5.2,3.8 Z" fill="#1b3f7a"/>
        </svg>
        555-374-9126
      </div>
    </div>
  </div>
</body>
</html>
```